1-3 PAGE WEBSITE LANDING PAGE DESIGN FOR CLIPRELAY.NET

I NEED A DESIGNER THAT HAS A GOOD UNDERSTANDING OF BUSINESS AND MARKETING SO HE CAN TAKE MY SALES SCRIPT AND CONVERT IT INTO A BEAUTIFUL IMAGE AND VIDEO FILLED WEBSITE THAT EXPLAINS EACH POINT BEAUTIFULLY. THE WEBSITE SHOULD BE EASY TO READ AND UNDERSTAND AND NAVIGATE.

PLEASE INCLUDE A EXAMPLES SECTION THAT CAN BE FILTERED BY INDUSTRY.

UNDER EVERY SECTION ON THE WEBSITE WE NEED TO HAVE A CALL TO ACTION BUTTON THAT WILL POP UP INTO A LEAD GEN FORM. THE BUTTON WILL SAY "SIGN UP FOR A FREE VIDEO AD MOCK UP FOR YOUR BUSINESS. No Purchase Necessary."

PLEASE SEE ATTACHED FILES FOR WORD DOC OF CONTENT AND LOGO FOR CLIPRELAY.NET

Target Market(s)

ALL BUSINESSES WHO WILL BE USING VIDEO ADVERTISEMENT AS PART OF THEIR OVERALL MARKETING STRATEGY FOR YEARS TO COME

Industry/Entity Type

Digital Marketing

Number of Pages Required

2 page

Colors

Designer to choose colors to be used in the design.

Requirements
Must have
• I would like color theme to coordinate with logo color theme
Nice to have
• must include all content included in word document

```html
<!DOCTYPE html>
<html lang="en">
<head>
<meta charset="utf-8">
<title>ClipRelay.net – Make A Promo Video</title>
<link rel="stylesheet" href="https://fonts.googleapis.com/css2?family=Roboto:wght@400;500;700;900&family=Montserrat:wght@400;500;600&display=swap">
<style>
:root{
  --yellow:#fdcd00;
  --teal:#00c0c8;
  --ink:#222;
  --muted:#444;
  --grey:#f2f2f2;
  --white:#fff;
  --black:#000;
}
*{box-sizing:border-box;margin:0;padding:0}
html,body{width:1200px;height:3933px;overflow:hidden}
body{position:relative;font-family:"Roboto",Arial,sans-serif;color:var(--ink);background:var(--white)}
.abs{position:absolute}
.bg{position:absolute;left:0;top:0;width:1200px;height:3933px}
/* header */
.lang{left:1063px;top:8px;font:500 12px "Roboto",sans-serif;display:flex;align-items:center;gap:6px}
.lang i{width:12px;height:12px;border:1.5px solid var(--teal);border-radius:50%}
.brand{left:50px;top:52px;font:900 30px "Roboto",sans-serif;color:var(--ink);letter-spacing:1px;display:flex;align-items:center;gap:8px}
.brand b{width:14px;height:14px;background:var(--yellow);border-radius:50%}
.nav{left:452px;top:58px;display:flex;gap:26px;font:400 15px "Montserrat",sans-serif;letter-spacing:1.5px;color:var(--ink);align-items:center}
.nav .signup{background:var(--teal);border-radius:6px;padding:10px 10px;margin-left:-10px}
/* buttons */
.btn{position:absolute;display:flex;align-items:center;justify-content:center;border-radius:30px;font-weight:700;color:var(--white);background:var(--teal)}
.btn.yellow{background:var(--yellow);border-radius:6px}
/* hero */
.hero-title{left:49px;top:162px;font:700 45px "Roboto",sans-serif;color:var(--white);letter-spacing:1.5px}
.hero-text{left:49px;top:255px;width:430px;font:700 20px/1.6 "Roboto",sans-serif;color:var(--white)}
.hero-media{left:575px;top:166px;width:578px;height:364px;border-radius:36px;overflow:hidden;background:linear-gradient(135deg,#c9ccc8,#7f8681 60%,#3f4240)}
.play-pill{left:706px;top:340px;width:320px;height:56px;border:4px solid var(--white);border-radius:30px;color:var(--white);font:700 20px "Roboto",sans-serif;display:flex;align-items:center;justify-content:center}
/* features */
.feat h2{position:absolute;font:500 31px/1.35 "Roboto",sans-serif;text-align:center;color:var(--ink)}
.feat p{position:absolute;font:400 13px/42px "Roboto",sans-serif;text-align:center;color:var(--muted)}
.dash{position:absolute;width:40px;height:3px;background:var(--yellow)}
/* reviews */
.sec-title{position:absolute;width:1200px;left:0;text-align:center;font:500 31px "Roboto",sans-serif}
.laptop-screen{left:374px;top:1328px;width:524px;height:352px;background:linear-gradient(120deg,#6f8a7e,#3e5a52 55%,#2c3d38)}
.laptop-frame{left:365px;top:1320px;width:542px;height:370px;border:10px solid #1d1d1f;border-radius:14px 14px 0 0}
.caption{color:var(--white);font:500 19px "Roboto",sans-serif}
.dot{position:absolute;left:1075px;width:13px;height:13px;border-radius:50%;background:var(--teal)}
.dot.ring{background:none;border:2px solid var(--teal)}
/* examples */
.tile{position:absolute;display:flex;align-items:flex-end;justify-content:center;color:var(--white);font:700 25px "Roboto",sans-serif;letter-spacing:1px;padding-bottom:22px}
/* option cards */
.thumb{position:absolute;border:2px solid #d8c300;width:324px;height:188px}
.opt h3{position:absolute;font:500 15px "Roboto",sans-serif;letter-spacing:2px}
.opt p{position:absolute;font:400 12px/20px "Roboto",sans-serif;color:var(--muted)}
.select{position:absolute;height:44px;width:324px;background:var(--teal);border-radius:4px;color:var(--white);font:700 16px "Roboto",sans-serif;padding:0 12px;display:flex;align-items:center;justify-content:space-between}
.news{left:815px;top:2742px;width:336px;height:346px;background:var(--teal)}
/* contact */
.label{position:absolute;font:500 11px "Roboto",sans-serif;color:var(--white)}
.field{position:absolute;background:var(--white);border:1px solid #ccc;border-radius:4px;font:400 12px "Roboto",sans-serif;color:#666;padding:0 8px;display:flex;align-items:center;height:36px}
/* footer */
.fcol{position:absolute;top:3700px}
.fcol h4{font:500 15px "Montserrat",sans-serif;letter-spacing:1px;margin-bottom:14px}
.fcol li{list-style:none;font:400 12px/27px "Montserrat",sans-serif;color:var(--muted);letter-spacing:.5px}
.social{left:48px;top:3760px;display:flex;gap:14px}
.social span{width:20px;height:20px;border:2px solid var(--ink);border-radius:3px}
.copy{left:0;top:3890px;width:1200px;height:43px;background:var(--black);color:var(--white);font:700 12px "Roboto",sans-serif;display:flex;align-items:center;justify-content:center;letter-spacing:.5px}
</style>
</head>
<body>
<svg class="bg" viewBox="0 0 1200 3933" aria-hidden="true">
  <!-- hero band -->
  <path d="M0 110H1200V700C1120 620 1040 585 900 575C720 560 580 605 430 640C260 680 120 670 0 515Z" fill="var(--yellow)"/>
  <circle cx="390" cy="570" r="15" fill="none" stroke="#fff" stroke-width="2"/>
  <circle cx="866" cy="538" r="12" fill="#fff"/>
  <circle cx="406" cy="117" r="5" fill="none" stroke="#fdcd00" stroke-width="1.5"/>
  <circle cx="1080" cy="600" r="5" fill="none" stroke="#fdcd00" stroke-width="1.5"/>
  <g fill="#fff"><circle cx="20" cy="380" r="2.5"/><circle cx="38" cy="392" r="2.5"/><circle cx="24" cy="404" r="2.5"/><circle cx="40" cy="410" r="2.5"/><circle cx="1184" cy="500" r="2.5"/><circle cx="1196" cy="524" r="2.5"/><circle cx="1178" cy="540" r="2.5"/></g>
  <!-- reviews band -->
  <path d="M0 1290C150 1140 380 1120 560 1145C760 1175 950 1205 1200 1110V1860C1050 1830 900 1860 650 1890C400 1920 200 1870 0 1730Z" fill="var(--grey)"/>
  <circle cx="237" cy="1481" r="137" fill="var(--yellow)"/>
  <circle cx="938" cy="1672" r="86" fill="var(--yellow)"/>
  <!-- contact band -->
  <path d="M0 3160C40 3280 120 3320 300 3330C500 3345 700 3300 900 3320C1060 3335 1140 3370 1200 3400V3650H0Z" fill="var(--yellow)"/>
</svg>

<header>
  <div class="abs lang"><i></i>English ▾</div>
  <div class="abs brand">CLIPRELAY.NET<b></b></div>
  <nav class="abs nav">
    <span>HOME</span><span>TEMPLATES</span><span>EXAMPLES ▾</span><span>PRODUCT</span><span>PRICING</span><span>LOGIN</span><span class="signup">SIGNUP</span>
  </nav>
</header>

<section class="hero">
  <h1 class="abs hero-title">Make A Promo Video!!</h1>
  <p class="abs hero-text">We are a video production company that specializes in short, entertaining mini commercial type of video “ADS” using premium stock footage</p>
  <a class="btn" style="left:49px;top:426px;width:379px;height:50px;font-size:14px">SIGN UP FOR A FREE VIDEO AD MOCK UP</a>
  <div class="abs hero-media" role="img" aria-label="Presenter speaking to a team in a meeting room"></div>
  <div class="abs play-pill">PLAY<span style="position:absolute;right:26px">›</span></div>
</section>

<section class="feat">
  <h2 style="left:49px;top:755px;width:425px">Fully Customized Video ADS<br>With Full Branding</h2>
  <div class="dash" style="left:242px;top:858px"></div>
  <p style="left:40px;top:872px;width:520px">We then fully customize the raw footage by adding content/text on<br>top of each transition/segment within the video ad. The transition/segment<br>is basically every time the text or an image or both change within the video.</p>
  <a class="btn" style="left:86px;top:1010px;width:367px;height:42px;font-size:13px">SIGN UP FOR A FREE VIDEO AD MOCK UP</a>

  <h2 style="left:700px;top:755px;width:460px">You Have Full Ownership<br>of Videos</h2>
  <div class="dash" style="left:910px;top:858px"></div>
  <p style="left:670px;top:872px;width:520px">The videos are fully licensed to you so you own them outright, 100%,<br>forever. All final video files are Full HD (1080p) in Mp4 Format.<br>we give you unlimited revisions</p>
  <a class="btn" style="left:744px;top:1011px;width:367px;height:42px;font-size:13px;font-weight:500">SIGN UP FOR A FREE VIDEO AD MOCK UP</a>
</section>

<section class="reviews">
  <h2 class="sec-title" style="top:1236px">Our Client Reviews</h2>
  <div class="dash" style="left:580px;top:1288px"></div>
  <div class="abs laptop-screen" role="img" aria-label="Client testimonial video still of two people talking"></div>
  <div class="abs laptop-frame"></div>
  <div class="abs" style="left:313px;top:1688px;width:646px;height:12px;background:linear-gradient(#c9c9cc,#6d6d70);border-radius:0 0 40px 40px"></div>
  <svg class="abs" style="left:580px;top:1463px" width="110" height="110" viewBox="0 0 110 110" aria-hidden="true"><circle cx="55" cy="55" r="50" fill="none" stroke="#fff" stroke-width="7"/><path d="M43 33L77 55L43 77Z" fill="none" stroke="#fff" stroke-width="7" stroke-linejoin="round"/></svg>
  <div class="abs caption" style="left:406px;top:1594px">Brightfizz Co.</div>
  <div class="abs caption" style="left:406px;top:1635px">Dana Holloway, Engagement Manager</div>
  <div class="dot ring" style="top:1441px"></div>
  <div class="dot" style="top:1480px"></div>
  <div class="dot" style="top:1519px"></div>
  <div class="dot" style="top:1558px"></div>
  <div class="dot" style="top:1597px"></div>
</section>

<section class="examples">
  <h2 class="sec-title" style="top:1911px">Our Video Work Examples</h2>
  <div class="dash" style="left:580px;top:1965px"></div>
  <div class="tile" style="left:49px;top:1992px;width:270px;height:611px;background:linear-gradient(160deg,#d9d9d9,#6b6b6b 55%,#2a2a2a)" role="img" aria-label="Hand holding a phone with a food delivery app">DASHPLATE</div>
  <div class="tile" style="left:319px;top:1992px;width:564px;height:295px;background:linear-gradient(180deg,#b9c4cc,#8b97a1 60%,#a44a4d)" role="img" aria-label="Man standing beside a red car">VANTOR</div>
  <div class="tile" style="left:319px;top:2287px;width:564px;height:316px;background:linear-gradient(120deg,#f6a400,#f06b1f 55%,#e8381f)" role="img" aria-label="Bag of spicy snack chips with chili peppers">CRUNCHWELL</div>
  <div class="tile" style="left:883px;top:1992px;width:270px;height:611px;background:linear-gradient(180deg,#5cc6d0,#4ab9c4)" role="img" aria-label="Illustrated crowd cheering a video marketing sign">MARKETING</div>
  <svg class="abs" style="left:0;top:0;pointer-events:none" width="1200" height="2700" aria-hidden="true">
    <g fill="none" stroke="#fff" stroke-width="7" stroke-linejoin="round">
      <circle cx="185" cy="2296" r="52"/><path d="M174 2274L204 2296L174 2318Z"/>
      <circle cx="600" cy="2146" r="52"/><path d="M589 2124L619 2146L589 2168Z"/>
      <circle cx="600" cy="2426" r="52"/><path d="M589 2404L619 2426L589 2448Z"/>
      <circle cx="1015" cy="2296" r="52"/><path d="M1004 2274L1034 2296L1004 2318Z"/>
    </g>
  </svg>
  <a class="btn" style="left:411px;top:2638px;width:378px;height:50px;font-size:20px;font-weight:500">TAKE ME TO VIDEO PORTFOLIO</a>
</section>

<section class="opt">
  <div class="thumb" style="left:57px;top:2741px;background:linear-gradient(120deg,#d6c7b0,#b75a4a 55%,#6d6a63)" role="img" aria-label="Man working at a laptop in a studio"></div>
  <div class="thumb" style="left:437px;top:2741px;background:linear-gradient(120deg,#4c5560,#23292f 60%,#14181b)" role="img" aria-label="Team meeting in a dark conference room"></div>
  <svg class="abs" style="left:0;top:2700px" width="800" height="260" aria-hidden="true">
    <g fill="none" stroke="#fff" stroke-width="7" stroke-linejoin="round">
      <circle cx="218" cy="135" r="52"/><path d="M207 113L237 135L207 157Z"/>
      <circle cx="599" cy="135" r="52"/><path d="M588 113L618 135L588 157Z"/>
    </g>
    <g fill="#fdcd00"><rect x="323" y="60" width="20" height="20" rx="4"/><rect x="323" y="86" width="20" height="20" rx="4"/><rect x="323" y="186" width="20" height="20" rx="4"/><rect x="709" y="60" width="20" height="20" rx="4"/><rect x="709" y="86" width="20" height="20" rx="4"/><rect x="709" y="186" width="20" height="20" rx="4"/></g>
  </svg>
  <h3 style="left:163px;top:2951px">VIDEO TYPE</h3>
  <p style="left:52px;top:2978px;width:300px">Select the type of video you would like to create from the drop down menu below:</p>
  <div class="select" style="left:49px;top:3040px">--Select Video Type--<span>▾</span></div>
  <a class="btn yellow" style="left:49px;top:3105px;width:324px;height:45px;font-size:13px">SIGN UP FOR A FREE VIDEO AD MOCK UP</a>

  <h3 style="left:546px;top:2951px">VIDEO USE CASE</h3>
  <p style="left:435px;top:2978px;width:300px">Select the type of video you would like to create from the drop down menu below:</p>
  <div class="select" style="left:430px;top:3040px">--Select Video Use Case--<span>▾</span></div>
  <a class="btn yellow" style="left:427px;top:3105px;width:324px;height:45px;font-size:13px">SIGN UP FOR A FREE VIDEO AD MOCK UP</a>

  <div class="abs news">
    <svg class="abs" style="left:145px;top:26px" width="44" height="32" viewBox="0 0 44 32" aria-hidden="true"><rect x="2" y="2" width="40" height="28" fill="none" stroke="#fff" stroke-width="3"/><path d="M2 2L22 18L42 2M2 30L17 15M42 30L27 15" fill="none" stroke="#fff" stroke-width="3"/></svg>
    <p class="abs" style="left:18px;top:84px;width:310px;font:700 15px/32px 'Roboto',sans-serif;color:#fff">Get the best Video Strategy news and ClipNote updates once a month straight to your inbox!</p>
    <div class="field" style="left:17px;top:188px;width:296px;height:44px;font-size:16px;color:#333;border-radius:0">Email Address</div>
    <a class="btn yellow" style="left:89px;top:274px;width:146px;height:35px;border-radius:20px;font-size:16px">Subscribe!</a>
  </div>
</section>

<section class="contact">
  <h2 class="abs" style="left:47px;top:3418px;font:700 26px 'Roboto',sans-serif;color:#fff">Let's talk Video!</h2>
  <p class="abs" style="left:48px;top:3458px;width:260px;font:400 12px/26px 'Roboto',sans-serif;color:#fff">You simply tell us what you want to promote and we deliver the video mockup in as little as 24 hours.</p>
  <span class="label" style="left:330px;top:3405px">First Name *</span>
  <div class="field" style="left:325px;top:3424px;width:243px">First Name</div>
  <span class="label" style="left:604px;top:3405px">Last Name *</span>
  <div class="field" style="left:598px;top:3424px;width:243px">Last Name</div>
  <span class="label" style="left:330px;top:3488px">Email *</span>
  <div class="field" style="left:323px;top:3507px;width:243px">Email</div>
  <span class="label" style="left:604px;top:3488px">Phone*</span>
  <div class="field" style="left:597px;top:3507px;width:243px">Phone</div>
  <span class="label" style="left:896px;top:3400px">Message *</span>
  <div class="field" style="left:890px;top:3421px;width:248px;height:116px;align-items:flex-start;padding-top:8px">Message</div>
  <a class="btn" style="left:897px;top:3566px;width:205px;height:36px;font-size:15px">Contact Us</a>
</section>

<footer>
  <div class="abs brand" style="top:3703px;font-size:27px">CLIPRELAY.NET<b></b></div>
  <div class="abs social"><span></span><span></span><span></span><span></span><span></span><span></span></div>
  <div class="fcol" style="left:284px"><h4>Company</h4><ul><li>About Us</li><li>Privacy Policy</li><li>Contact Us</li><li>Blog</li></ul></div>
  <div class="fcol" style="left:465px"><h4>Product</h4><ul><li>Pricing guide</li><li>Try Our Template</li><li>Customers</li><li>Product Updates</li></ul></div>
  <div class="fcol" style="left:644px"><h4>Support</h4><ul><li>Video Learn</li><li>Help Center</li><li>Terms and Condition</li><li>Affiliates</li></ul></div>
  <div class="fcol" style="left:853px"><h4>Community</h4><ul><li>Blog</li><li>Friendwall</li><li>Chirpline</li><li>Viewtube</li></ul></div>
  <div class="fcol" style="left:1030px"><h4>Solutions</h4><ul><li>Marketing Agency</li><li>Intro Videos</li><li>Explainer Videos</li><li>recruitment Videos</li></ul></div>
  <div class="abs copy">©CopyRight @2019, All Rights Reserved</div>
</footer>
</body>
</html>
```